Building Certification Company needs a professional letterhead and report template

We are a modern company within an ageing industry. Our industry is responsible for life safety aspects of the built environment, we ensure buildings are safe and fit for occupation.

We use letterhead and reports everyday, we need a smart and professional letterhead that reflects the serious nature of the work we do. We also require a report template of the same ilk.

Target Market(s)

Our target market will consist mainly of professional architects, developers and construction companies.

Industry/Entity Type

Industry

Requirements
Must have
• The letterhead must have:-
Our logo
Our company details, including address, website, email, phone

Address - Suite 208 / 45 Harwick Lane Dunmore NSW 2100

Website - www.quillstonecompliance.example.au

Email - info@qsc.example.au

Phone - 02 5550 3846

The report template must have:-
A title page, which is to incorporate our logo or an aspect of our logo, get creative people.

```html
<!DOCTYPE html>
<html lang="en">
<head>
<meta charset="utf-8">
<title>Quillstone Compliance Letterhead</title>
<link href="https://fonts.googleapis.com/css2?family=Montserrat:wght@700&family=Open+Sans:wght@400;600&display=swap" rel="stylesheet">
<style>
  :root {
    --backdrop: #e6e7ea;
    --paper: #ffffff;
    --navy: #2b3f78;
    --accent: #4a66b8;
    --slate: #6b7682;
    --slate-light: #9aa3ad;
    --ink: #3a3f46;
  }
  * { margin: 0; padding: 0; box-sizing: border-box; }
  html, body {
    width: 1200px; height: 874px; overflow: hidden;
    background: var(--backdrop);
  }
  .letterhead {
    position: absolute; left: 310px; top: 27px;
    width: 580px; height: 820px;
    background: var(--paper);
    box-shadow: 0 4px 18px rgba(0,0,0,0.12);
    font-family: "Open Sans", Arial, sans-serif;
    color: var(--ink);
  }
  .brand {
    position: absolute; left: 44px; top: 48px;
    display: flex; align-items: center; gap: 10px;
  }
  .brand-square { width: 26px; height: 26px; background: var(--navy); }
  .brand-name {
    font-family: "Open Sans", Arial, sans-serif; font-weight: 600;
    font-size: 19px; color: var(--navy); letter-spacing: 0.5px;
  }
  .letter-body {
    position: absolute; left: 44px; top: 140px; width: 470px;
    font-size: 8.6px; line-height: 1.5;
  }
  .letter-body p { margin-bottom: 10px; }
  .divider {
    position: absolute; left: 44px; top: 612px; width: 492px; height: 3px;
    background: linear-gradient(to right, var(--slate-light) 0 78%, var(--accent) 78% 100%);
  }
  .contact-line {
    position: absolute; left: 44px; right: 44px; top: 700px;
    text-align: right; font-size: 8px; color: var(--slate);
  }
  .contact-line span + span::before { content: " | "; color: var(--slate-light); }
  .contact-line strong { font-weight: 600; color: var(--navy); }
  .footer-band {
    position: absolute; left: 0; right: 0; bottom: 22px; height: 12px;
    background: linear-gradient(to right, var(--accent) 0 14%, var(--slate) 14% 100%);
  }
</style>
</head>
<body>
  <main class="letterhead">
    <header class="brand">
      <div class="brand-square"></div>
      <div class="brand-name">QUILLSTONE COMPLIANCE</div>
    </header>

    <section class="letter-body">
      <p>18 Carrow Street<br>Dunmore, NSW 2100</p>
      <p>January 15th, 2024</p>
      <p>Ms. Jane Harlow<br>Director, Harlow Design Group<br>12 Ferrier Road<br>Kiama NSW 2533</p>
      <p>Dear Ms. Harlow,</p>
      <p>Thank you for choosing us to assess your new residential project on Ferrier Road. This letter confirms that our certifier will inspect the site next week. The visit covers fire safety, egress paths and structural compliance with the current code. Please ensure site access is arranged and plans are ready.</p>
      <p>Our final report will follow within five working days of the inspection.</p>
      <p>Sincerely,</p>
      <p>Signed on behalf of the certification team</p>
      <p>Peter Ashby<br>Director, Quillstone Compliance</p>
    </section>

    <div class="divider"></div>

    <footer class="contact-line">
      <span><strong>Address:</strong> Suite 208 / 45 Harwick Lane Dunmore NSW 2100</span><br>
      <span><strong>Website:</strong> www.quillstonecompliance.example.au</span><span><strong>Email:</strong> info@qsc.example.au</span><span><strong>Phone:</strong> 02 5550 3846</span>
    </footer>

    <div class="footer-band"></div>
  </main>
</body>
</html>
```